Create a beautiful brochure for a Permanent Make Up Clinic

I need a classy brochure for my Permanent Make up Clinic. It needs a classy cover and the list of services and extra information on the inside. I don't have any requirements on size of the brochure, but it needs to look attractive and upmarket. The colors I like are black -white - Gold - grey. I like a minimalistic look.
I’d like to have my logo on the cover, the price list on the inside and the address information at the back.

Target Market(s)

woman between 18 and 99 years old

Industry/Entity Type

Beauty

Font styles to use
Sans Serif
Script

Colors

Designer to choose colors to be used in the design.

Requirements
Must have
• the logo on the cover
• pictures of the services with an explanation and pricing
• address information at the back
Nice to have
• a classy upmarket look, not with too many different colors in it.

```html
<!DOCTYPE html>
<html lang="nl">
<head>
<meta charset="utf-8">
<title>Velora Clinic – Permanent Make Up brochure</title>
<link href="https://fonts.googleapis.com/css2?family=Jost:wght@400;500;600&display=swap" rel="stylesheet">
<style>
  :root {
    --stage: #9a9a9a;
    --paper: #ffffff;
    --ink: #2b2b2b;
    --black: #1f1d1b;
    --gold: #c9a45c;
    --gold-soft: #e0c585;
    --muted-white: #e9e6e1;
  }
  * { box-sizing: border-box; margin: 0; padding: 0; }
  html, body { width: 1200px; height: 800px; overflow: hidden; }
  body {
    background: radial-gradient(circle at 50% 40%, #b4b4b4, var(--stage) 75%);
    font-family: "Jost", "Futura", sans-serif;
    color: var(--ink);
  }
  .brochure {
    position: absolute; left: 60px; top: 60px;
    width: 1080px; height: 680px;
    display: flex;
    box-shadow: 0 18px 40px rgba(0,0,0,.35);
  }
  .panel { width: 360px; height: 680px; position: relative; overflow: hidden; }

  /* Panel 1 – intro */
  .panel--intro { background: var(--paper); }
  .intro__text { padding: 26px 28px 0 30px; }
  .intro__title { color: var(--gold); font-weight: 500; font-size: 21px; line-height: 1.15; margin-bottom: 12px; }
  .body-copy { font-size: 9.5px; line-height: 1.45; }
  .intro__subtitle { color: var(--gold); font-weight: 500; font-size: 13px; line-height: 1.2; margin: 12px 0 8px; }
  .checklist { list-style: none; }
  .checklist li { display: flex; gap: 7px; font-size: 9.5px; line-height: 1.4; margin-bottom: 5px; }
  .checklist svg { flex: none; margin-top: 2px; }
  .intro__concept { font-size: 10.5px; font-weight: 600; line-height: 1.35; margin-top: 10px; }
  .intro__photo {
    position: absolute; left: 0; bottom: 0; width: 360px; height: 225px;
    background: linear-gradient(120deg, #1d1b1a 0%, #3a2e2a 40%, #c99c88 70%, #e2bfae 100%);
  }

  /* Panel 2 – services */
  .panel--services { background: var(--black); color: var(--muted-white); padding: 26px 28px 0 28px; }
  .services__title { color: var(--gold); font-weight: 500; font-size: 14px; line-height: 1.25; margin-bottom: 14px; }
  .service { margin-bottom: 13px; }
  .service__head { display: flex; justify-content: space-between; align-items: flex-end; gap: 10px; }
  .service__name { color: var(--gold); font-weight: 500; font-size: 12px; }
  .price-tag {
    background: var(--gold-soft); color: var(--black);
    font-size: 10px; font-weight: 500; padding: 1px 10px; min-width: 48px; text-align: center;
  }
  .service__price-row { display: flex; justify-content: flex-end; margin-bottom: 3px; }
  .service__text { font-size: 9.5px; line-height: 1.45; margin-top: 4px; }

  /* Panel 3 – consult */
  .panel--consult { background: var(--paper); }
  .consult__photo-main {
    height: 200px;
    background: linear-gradient(135deg, #6b4a3a 0%, #c8a48e 45%, #d59fc4 75%, #7e7fa8 100%);
  }
  .consult__photo-row { display: flex; height: 82px; gap: 2px; margin-top: 2px; }
  .consult__photo-row div { flex: 1; }
  .thumb--brows { background: linear-gradient(135deg, #b28c74, #d8b7a0); }
  .thumb--eyes { background: linear-gradient(135deg, #8c6d5e, #c9a593); }
  .thumb--lips { background: linear-gradient(135deg, #c7787c, #e8b5ae); }
  .consult__body { padding: 26px 30px 0; }
  .consult__badge {
    display: block; margin: 0 auto 22px; width: 230px;
    background: var(--black); color: var(--gold-soft);
    border: 2px solid var(--gold); border-radius: 30px;
    text-align: center; font-size: 15px; font-weight: 500; letter-spacing: .5px; padding: 6px 0;
  }
  .consult__text { font-size: 9.5px; line-height: 1.5; margin-bottom: 22px; }
  .consult__web { text-align: right; font-size: 13px; font-weight: 600; margin-top: 34px; }
</style>
</head>
<body>
<main class="brochure">

  <section class="panel panel--intro">
    <div class="intro__text">
      <h1 class="intro__title">Permanent Make Up,<br>de behandeling die<br>elke vrouw verdient.</h1>
      <p class="body-copy">Bij een permanente makeup behandeling worden kleuren met een dunne naald gepigmenteerd in de bovenste huidlagen. Velora Clinic gebruikt alleen geteste en hoogwaardige producten van de marktleider in permanente makeup.</p>
      <h2 class="intro__subtitle">Velora Clinic garandeert absolute steriliteit<br>en veiligheid tijdens elke behandeling:</h2>
      <ul class="checklist">
        <li><svg width="9" height="9" viewBox="0 0 10 10"><path d="M1 5l3 3 5-7" fill="none" stroke="#c9a45c" stroke-width="1.6"/></svg>De steriele naald voor eenmalig gebruik wordt vóór elke behandeling opnieuw geopend.</li>
        <li><svg width="9" height="9" viewBox="0 0 10 10"><path d="M1 5l3 3 5-7" fill="none" stroke="#c9a45c" stroke-width="1.6"/></svg>Alle oppervlakken worden regelmatig schoongemaakt met speciale desinfecterende oplossingen.</li>
        <li><svg width="9" height="9" viewBox="0 0 10 10"><path d="M1 5l3 3 5-7" fill="none" stroke="#c9a45c" stroke-width="1.6"/></svg>Tijdens elke behandeling een wordt een beschermend masker, handschoenen en werkkleding gedragen.</li>
        <li><svg width="9" height="9" viewBox="0 0 10 10"><path d="M1 5l3 3 5-7" fill="none" stroke="#c9a45c" stroke-width="1.6"/></svg>De vereisten van de Belgische wetgeving ivm hygiëne worden geïmplementeerd in de Velora Clinic.</li>
      </ul>
      <p class="intro__concept">Het concept bij Velora Clinic is fundamenteel anders dan het verouderde idee van een overdreven make up. In plaats van een kunstig masker te creëren, ziet het er natuurlijk uit met behulp van de nieuwste permanente make up technieken.</p>
    </div>
    <div class="intro__photo" role="img" aria-label="Portretfoto van een vrouw met roze lippen en gelakte nagels"></div>
  </section>

  <section class="panel panel--services">
    <h2 class="services__title">We bekijken samen de meest geschikte<br>techniek voor u:</h2>

    <article class="service">
      <div class="service__head"><h3 class="service__name">Powder Brows Magic Shading techniek:</h3><span class="price-tag">€320</span></div>
      <p class="service__text">De meest natuurlijke techniek voor wenkbrauwen. Met een zeer fijne nanonaald worden er kleine puntjes in de huid op de wenkbrauwen geplaatst en gevuld met pigment. Het gevolg is dat het resultaat niet strak en donker is, maar er zacht uitziet als een licht wenkbrauwpoeder. De contouren zijn niet strak maar zeer zacht.</p>
    </article>

    <article class="service">
      <div class="service__price-row"><span class="price-tag">€490</span></div>
      <h3 class="service__name">Full Lips Aquarelle Techniek</h3>
      <p class="service__text">Deze techniek corrigeert (indien nodig) optisch asymmetrische of onregelmatige lipcontouren. Je kan nog lippenstift aanbrengen, maar deze ga je niet meer nodig hebben! Een kleurloze lippenbalsem geeft je lippen glans en zachtheid.</p>
    </article>

    <article class="service">
      <div class="service__price-row"><span class="price-tag">€235</span></div>
      <h3 class="service__name">Klassieke eyeliner</h3>
      <p class="service__text">Deze eyeliner is een klassieke permanente make up techniek. Door de contouren van de oogleden te accentueren lijken uw ogen groter, helderder en meer alert.</p>
    </article>

    <article class="service">
      <div class="service__price-row"><span class="price-tag">€235</span></div>
      <h3 class="service__name">Soft eyeliner</h3>
      <p class="service__text">Aan het bovenste ooglid wordt er een speciale schaduwtechniek te gebruikt. Door deze pigmentatie lijkt het ooglid na genezing te zijn geschilderd met oogschaduw. Deze schaduwtechniek is ideaal voor een natuurlijk oogaccent.</p>
      <p class="service__text">U kunt de lengte en breedte van de eyeliner en de intensiteit van de oogschaduw zelf kiezen!</p>
    </article>

    <article class="service">
      <div class="service__price-row"><span class="price-tag">€189</span></div>
      <h3 class="service__name">Eyeliner onder het oog</h3>
      <p class="service__text">De fijne eyeliner om uw ogen op een subtiele manier iets meer accentueren en laten spreken.</p>
    </article>
  </section>

  <section class="panel panel--consult">
    <div class="consult__photo-main" role="img" aria-label="Foto van een specialiste die een wenkbrauwbehandeling uitvoert"></div>
    <div class="consult__photo-row">
      <div class="thumb--brows" role="img" aria-label="Detailfoto van behandelde wenkbrauwen"></div>
      <div class="thumb--eyes" role="img" aria-label="Detailfoto van een oog met eyeliner"></div>
      <div class="thumb--lips" role="img" aria-label="Detailfoto van gepigmenteerde lippen"></div>
    </div>
    <div class="consult__body">
      <span class="consult__badge">GRATIS ADVIESGESPREK</span>
      <p class="consult__text">Het is mogelijk om eerst op consult te komen om te bespreken wat je graag zou willen. De gewenste vorm van uw wenkbrauwen, lippen of eyeliner word samen uitgetekend, we zoeken dan samen de kleur uit die jou gezicht het beste ophaalt en het mooiste bij je past, zodat je een idee krijgt van het resultaat.</p>
      <p class="consult__text">De huid wordt verdoofd door een efficiënte en huidvriendelijke crème, die pijnloze pigmentatie mogelijk maakt.</p>
      <p class="consult__web">www.veloraclinic.be</p>
    </div>
  </section>

</main>
</body>
</html>
```